RW Soundworks Web Site Design

Need a basic site to show clients a little about what we do. We are a custom audio video company in the high-end residential market. Need a few basic but professional pages to show past projects and products we sell. No e-commerce. Should include my new logo from MarkHive.

Industry/Entity Type

Residential

Number of Pages Required

2 page

Font styles to use
Serif
Sans Serif

Colors
f78f20

Requirements
Must have
• Company Logo, Send feedback page
Nice to have
• I have no ideas about design, but I do know what I like and dislike when I see it.

```html
<!DOCTYPE html>
<html lang="en">
<head>
<meta charset="utf-8">
<title>RW Soundworks</title>
<link href="https://fonts.googleapis.com/css2?family=Lato:wght@300;400;700&display=swap" rel="stylesheet">
<style>
:root{
  --orange:#f78f20;
  --dark:#222222;
  --text:#333333;
  --muted:#555555;
  --light-bg:#ececec;
  --project-bg:#666666;
  --footer-bg:#2b2b2b;
  --bottom-bg:#141414;
  --line:#999999;
}
*{margin:0;padding:0;box-sizing:border-box}
html,body{width:674px;height:1200px;overflow:hidden;background:#fff}
body{font-family:'Lato',sans-serif;color:var(--text);position:relative}
.abs{position:absolute}

/* header */
.header{left:0;top:0;width:674px;height:30px;background:#fff}
.brand{left:70px;top:0;width:168px;height:53px;background:#fff;z-index:3;display:flex;align-items:center;gap:8px;padding-left:12px}
.brand-mark{width:22px;height:22px;background:var(--orange)}
.brand-name{font-size:15px;font-weight:700;color:var(--dark);letter-spacing:.5px;line-height:1}
.feedback-btn{left:422px;top:5px;width:52px;height:16px;border:1px solid var(--orange);font-size:6.5px;font-weight:700;display:flex;align-items:center;justify-content:center;color:var(--dark)}
.call{left:504px;top:2px;display:flex;align-items:center;gap:6px}
.call-label{font-size:7.5px;letter-spacing:1.5px;color:var(--dark)}
.call-number{font-size:11px;color:var(--dark);letter-spacing:.3px}
.nav{left:0;top:30px;width:674px;height:28px;background:var(--dark)}
.nav ul{list-style:none;position:absolute;left:250px;top:0;display:flex;height:28px}
.nav li{font-size:8.5px;font-weight:700;color:#fff;display:flex;align-items:center;justify-content:center;border-right:1px solid #444;height:28px}
.nav li.active{background:var(--orange)}

/* hero */
.hero{left:0;top:58px;width:674px;height:236px;background:linear-gradient(180deg,#f39a2a 0%,#ef8a1a 55%,#d86a14 100%)}
.hero-band{left:0;top:203px;width:674px;height:33px;background:linear-gradient(180deg,rgba(60,20,10,.55),rgba(40,10,5,.8))}
.hero-title{left:0;top:203px;width:674px;height:33px;text-align:center;font-size:24px;color:#f9b34a;line-height:33px;text-shadow:0 1px 3px rgba(0,0,0,.6)}

/* section titles */
.sec-title{width:674px;left:0;text-align:center;font-size:24px;font-weight:400;letter-spacing:.3px;color:var(--text)}
.sec-title .hl{color:var(--orange)}
.divider{left:0;width:674px;height:8px}
.divider .l{position:absolute;top:3px;height:1px;background:var(--line)}
.divider .m{position:absolute;left:333px;top:0;width:8px;height:8px;background:var(--orange);transform:rotate(45deg)}

/* welcome */
.welcome-kicker{left:0;top:318px;width:674px;text-align:center;font-size:16px;color:var(--orange)}
.welcome-title{left:0;top:336px;width:674px;text-align:center;font-size:24px;color:var(--text);letter-spacing:.3px}
.welcome-text{left:134px;top:386px;width:406px;text-align:center;font-size:7.4px;line-height:13.5px;color:var(--text)}
.read-more{left:311px;top:435px;width:52px;height:16px;border:1px solid var(--orange);border-radius:2px;font-size:6px;font-weight:700;display:flex;align-items:center;justify-content:center}

/* services */
.services{left:0;top:478px;width:674px;height:220px;background:var(--light-bg)}
.svc{top:554px;width:104px;text-align:center}
.svc-icon{width:64px;height:64px;margin:0 auto;border-radius:50%;background:#111;border:3px solid #fff;box-shadow:0 0 3px rgba(0,0,0,.25);display:flex;align-items:center;justify-content:center}
.svc-icon.orange{background:var(--orange)}
.svc-name{margin-top:9px;font-size:8.5px;font-weight:700;line-height:10.5px;color:var(--text)}
.svc-text{margin-top:8px;font-size:6.6px;line-height:10.5px;color:var(--muted)}
.svc-sep{top:556px;width:1px;height:130px;background:#dcdcdc}
.arrow{width:12px;height:20px}
.shadow{left:70px;width:534px;height:12px;background:radial-gradient(ellipse at top,rgba(0,0,0,.22),rgba(0,0,0,0) 70%)}

/* projects */
.projects{left:0;top:720px;width:674px;height:200px;background:var(--project-bg)}
.projects .sec-title{color:#e6e6e6}
.project{top:803px;width:123px;height:80px;border:3px solid #fff;box-shadow:0 2px 4px rgba(0,0,0,.4)}

/* contact */
.field{height:19px;border:1px solid #555;border-radius:2px;font-size:6.5px;color:#aaa;padding:5px 12px}
.submit{left:513px;top:1052px;width:51px;height:17px;border:1px solid var(--orange);border-radius:2px;font-size:8px;font-weight:700;display:flex;align-items:center;justify-content:center}

/* footer */
.footer{left:0;top:1094px;width:674px;height:80px;background:var(--footer-bg)}
.foot-nav{left:0;top:1103px;width:674px;display:flex;justify-content:center;font-size:7.5px;color:#ddd}
.foot-nav span{padding:0 13px;border-left:1px solid #aaa;line-height:9px}
.foot-nav span:last-child{border-right:1px solid #aaa}
.foot-nav .active{color:var(--orange)}
.foot-info{font-size:7px;line-height:9px;color:#eee;display:flex;gap:5px}
.social{top:1144px;width:13px;height:13px;background:#fff}
.social.o{background:var(--orange)}
.foot-brand{left:482px;top:1128px;display:flex;align-items:center;gap:6px;font-size:12px;font-weight:700;color:#9a9a9a;letter-spacing:.4px}
.foot-brand i{width:18px;height:18px;background:#8a8a8a;display:block}
.bottom{left:0;top:1174px;width:674px;height:26px;background:var(--bottom-bg);color:#ddd;font-size:7px;text-align:center;line-height:26px}
</style>
</head>
<body>

<header>
  <div class="abs header"></div>
  <div class="abs brand"><span class="brand-mark"></span><span class="brand-name">RW SOUNDWORKS</span></div>
  <div class="abs feedback-btn">FEEDBACK</div>
  <div class="abs call">
    <svg width="20" height="20" viewBox="0 0 20 20"><circle cx="10" cy="10" r="9" fill="none" stroke="#f78f20" stroke-width="1.3"/><path d="M7 5.5l2 2-1 1.3c.6 1.3 1.6 2.3 2.9 2.9l1.3-1 2 2-1.3 1.5C9.8 14 6 10.2 5.8 6.8z" fill="#f78f20"/></svg>
    <div><div class="call-label">CALL US TODAY</div><div class="call-number">555-014-2290</div></div>
  </div>
  <nav class="abs nav">
    <ul>
      <li class="active" style="width:45px">HOME</li>
      <li style="width:62px">ABOUT US</li>
      <li style="width:96px">Product &amp; Services</li>
      <li style="width:74px">Past Projects</li>
      <li style="width:72px">CONTACT US</li>
    </ul>
  </nav>
</header>

<section>
  <div class="abs hero" role="img" aria-label="Home theatre room with wall-mounted television, speakers and red lounge chairs on an orange wall"></div>
  <div class="abs hero-band"></div>
  <h1 class="abs hero-title" style="font-weight:400">We Are Custom Audio Video Company</h1>
</section>

<section>
  <div class="abs welcome-kicker">WELCOME TO</div>
  <h2 class="abs welcome-title" style="font-weight:400">RW SOUNDWORKS</h2>
  <div class="abs divider" style="top:366px"><span class="l" style="left:233px;width:84px"></span><span class="m"></span><span class="l" style="left:360px;width:82px"></span></div>
  <p class="abs welcome-text">Lorem Ipsum Dolor Sit Amet, Consectetur Adipiscing Elit. Aenean Sodales Diam Quis Velit Pellentesque Vehicula. Donec Luctus Justo Aliquet Est Volutpat, Sedtincidunt Odio Pretium. Sed Id Est Ultrici Rutrum Arcu Pretium, Porttitor Enim. Integer Quis Luctus Ligula. Donec Id Scelerisque Lorem.</p>
  <div class="abs read-more">READ MORE »</div>
</section>

<section>
  <div class="abs services"></div>
  <h2 class="abs sec-title" style="top:497px"><span class="hl">OUR</span> SERVICES</h2>
  <div class="abs divider" style="top:530px"><span class="l" style="left:287px;width:37px"></span><span class="m"></span><span class="l" style="left:351px;width:36px"></span></div>

  <svg class="abs arrow" style="left:29px;top:608px" viewBox="0 0 12 20"><path d="M10 2L2 10l8 8" fill="none" stroke="#444" stroke-width="1.6"/></svg>
  <svg class="abs arrow" style="left:633px;top:608px" viewBox="0 0 12 20"><path d="M2 2l8 8-8 8" fill="none" stroke="#444" stroke-width="1.6"/></svg>

  <div class="abs svc" style="left:65px">
    <div class="svc-icon orange"><svg width="34" height="28" viewBox="0 0 34 28"><rect x="10" y="10" width="20" height="13" fill="none" stroke="#fff" stroke-width="2"/><path d="M18 14v6l5-3z" fill="#fff"/><circle cx="9" cy="9" r="6" fill="none" stroke="#fff" stroke-width="2"/></svg></div>
    <div class="svc-name">Distributed<br>Video</div>
    <div class="svc-text">Lorem ipsum dolor si amet consectetur adipiscing elit Etiam feugiat urna leo</div>
  </div>
  <div class="abs svc-sep" style="left:171px"></div>
  <div class="abs svc" style="left:174px">
    <div class="svc-icon"><svg width="34" height="30" viewBox="0 0 34 30"><rect x="3" y="3" width="14" height="22" fill="none" stroke="#fff" stroke-width="2"/><rect x="13" y="12" width="18" height="12" fill="#111" stroke="#fff" stroke-width="2"/><path d="M6 8h8M6 12h5M6 16h5" stroke="#fff" stroke-width="1.5"/></svg></div>
    <div class="svc-name">Media<br>Rooms</div>
    <div class="svc-text">Lorem ipsum dolor si amet consectetur adipiscing elit Etiam feugiat urna leo</div>
  </div>
  <div class="abs svc-sep" style="left:281px"></div>
  <div class="abs svc" style="left:285px">
    <div class="svc-icon"><svg width="34" height="30" viewBox="0 0 34 30"><rect x="6" y="2" width="22" height="15" fill="none" stroke="#fff" stroke-width="2"/><path d="M14 6v7l6-3.5z" fill="#fff"/><rect x="5" y="20" width="24" height="7" fill="#fff"/></svg></div>
    <div class="svc-name">Residential<br>Cinemas</div>
    <div class="svc-text">Lorem ipsum dolor si amet consectetur adipiscing elit Etiam feugiat urna leo</div>
  </div>
  <div class="abs svc-sep" style="left:390px"></div>
  <div class="abs svc" style="left:394px">
    <div class="svc-icon"><svg width="34" height="30" viewBox="0 0 34 30"><path d="M6 14L17 4l11 10v12H6z" fill="#fff"/><rect x="14" y="18" width="6" height="8" fill="#111"/></svg></div>
    <div class="svc-name">Whole-House<br>Control Systems</div>
    <div class="svc-text">Lorem ipsum dolor si amet consectetur adipiscing elit Etiam feugiat urna leo</div>
  </div>
  <div class="abs svc-sep" style="left:500px"></div>
  <div class="abs svc" style="left:505px">
    <div class="svc-icon"><svg width="34" height="30" viewBox="0 0 34 30"><circle cx="21" cy="18" r="7" fill="#fff"/><path d="M10 2v8M14 2v8M8 10h8v4h-8zM12 14v6h5" stroke="#fff" stroke-width="2" fill="none"/></svg></div>
    <div class="svc-name">Automated<br>Lighting Control</div>
    <div class="svc-text">Lorem ipsum dolor si amet consectetur adipiscing elit Etiam feugiat urna leo</div>
  </div>
  <div class="abs shadow" style="top:698px"></div>
</section>

<section>
  <div class="abs projects"></div>
  <h2 class="abs sec-title" style="top:739px;font-weight:300;color:#e8e8e8"><span class="hl">PAST</span> PROJECTS</h2>
  <div class="abs divider" style="top:772px"><span class="l" style="left:271px;width:47px"></span><span class="m"></span><span class="l" style="left:357px;width:56px"></span></div>
  <svg class="abs arrow" style="left:48px;top:833px" viewBox="0 0 12 20"><path d="M10 2L2 10l8 8" fill="none" stroke="#fff" stroke-width="1.6"/></svg>
  <svg class="abs arrow" style="left:614px;top:833px" viewBox="0 0 12 20"><path d="M2 2l8 8-8 8" fill="none" stroke="#fff" stroke-width="1.6"/></svg>
  <div class="abs project" style="left:74px;background:linear-gradient(180deg,#2b3a6a,#6a3a2a 60%,#3a2a22)" role="img" aria-label="Restaurant bar with multiple wall-mounted televisions"></div>
  <div class="abs project" style="left:209px;background:linear-gradient(180deg,#8a2a1e,#5a1c14 60%,#2a1a14)" role="img" aria-label="Private home cinema room with red walls and recliners"></div>
  <div class="abs project" style="left:343px;background:linear-gradient(90deg,#d9c4b0,#e8e6e2 60%,#cfd3d6)" role="img" aria-label="Homeowner using a wall-mounted touch control panel"></div>
  <div class="abs project" style="left:478px;background:linear-gradient(180deg,#3a3a3a,#7a5a4a 55%,#1e1e1e)" role="img" aria-label="Hand operating a touchscreen home control interface"></div>
  <div class="abs shadow" style="top:920px"></div>
</section>

<section>
  <h2 class="abs sec-title" style="top:939px"><span class="hl">QUICK</span> CONTACT</h2>
  <div class="abs divider" style="top:972px"><span class="l" style="left:272px;width:45px"></span><span class="m"></span><span class="l" style="left:357px;width:56px"></span></div>
  <div class="abs field" style="left:74px;top:999px;width:169px">Name</div>
  <div class="abs field" style="left:252px;top:999px;width:170px">Mob</div>
  <div class="abs field" style="left:430px;top:999px;width:170px">Email</div>
  <div class="abs field" style="left:74px;top:1024px;width:432px;height:45px">Message</div>
  <div class="abs submit">SUBMIT</div>
</section>

<footer>
  <div class="abs footer"></div>
  <div class="abs foot-nav"><span class="active">Home</span><span>About Us</span><span>Product &amp; Services</span><span>Past Projects</span><span>Feedback</span><span>Contact Us</span></div>
  <div class="abs foot-info" style="left:73px;top:1131px">
    <svg width="7" height="9" viewBox="0 0 7 9"><path d="M3.5 0A3.2 3.2 0 0 0 .3 3.2C.3 5.5 3.5 9 3.5 9s3.2-3.5 3.2-5.8A3.2 3.2 0 0 0 3.5 0z" fill="#fff"/><circle cx="3.5" cy="3.2" r="1.2" fill="#2b2b2b"/></svg>
    <div>Lorem Ipsum,<br>Dolor sit amet consectetuer,<br>Adipiscing - 12345</div>
  </div>
  <div class="abs foot-info" style="left:211px;top:1131px">
    <svg width="8" height="8" viewBox="0 0 8 8"><path d="M1 .5l2 2-1 1.2c.6 1 1.3 1.7 2.3 2.3l1.2-1 2 2-1 1.5C3 8 0 5 .2 1.5z" fill="#fff"/></svg>
    <div>Phone: 0555 014 229</div>
  </div>
  <div class="abs foot-info" style="left:211px;top:1148px">
    <svg width="10" height="7" viewBox="0 0 10 7"><rect width="10" height="7" fill="#fff"/><path d="M0 0l5 4 5-4" stroke="#2b2b2b" fill="none"/></svg>
    <div>info@rwsoundworks.com</div>
  </div>
  <div class="abs social o" style="left:377px"></div>
  <div class="abs social" style="left:397px"></div>
  <div class="abs social" style="left:417px"></div>
  <div class="abs social" style="left:437px"></div>
  <div class="abs foot-brand"><i></i>RW SOUNDWORKS</div>
  <div class="abs bottom">© 2015 RWSoundworksAudioVideo &nbsp;|&nbsp; All rights reserved</div>
</footer>

</body>
</html>
```